New Business Card : Logo provided (black&red)

Use logo to ascertain colours.
Front of card :
Logo
Director : Darren Kellworth
ABN : 47302961
T : 0458 712 064
E : trimvolt@pelmarix.com
W : trimvoltfitness.net.au

Back of card :
Outdoor Group Training
Harrowvale Rowing Club
42 Pellinore Road
Scarborough WA 6019

Personal Training
Greywater Bay Fitness Studio
518 Marrowdene Street
Scarborough WA 6019

Logo's attached are low resolution apparently so will look into why that is and update as soon as I can.  

Logo's updated.

```html
<!DOCTYPE html>
<html lang="en">
<head>
<meta charset="utf-8">
<title>Trimvolt Fitness – Business Card</title>
<link href="https://fonts.googleapis.com/css2?family=Jost:wght@400;500;700&display=swap" rel="stylesheet">
<style>
  :root {
    --red: #e8202a;
    --red-light: #f0533f;
    --red-deep: #d8141f;
    --black: #1a1a1a;
    --grey: #555555;
    --paper: #fbfbfb;
    --backdrop: #e9e7e3;
    --white: #ffffff;
  }
  * { margin: 0; padding: 0; box-sizing: border-box; }
  html, body {
    width: 1200px; height: 900px; overflow: hidden;
    background: var(--backdrop);
    font-family: "Jost", "Futura", sans-serif;
  }
  .canvas { position: relative; width: 1200px; height: 900px; }
  .card {
    position: absolute; width: 660px; height: 403px;
    overflow: hidden; border-radius: 3px;
    box-shadow: 0 6px 18px rgba(0,0,0,0.18);
  }
  .brand {
    display: flex; align-items: center; gap: 10px;
    font-weight: 700; font-size: 26px; letter-spacing: 1px;
    color: var(--black); white-space: nowrap;
  }
  .brand__dot {
    width: 28px; height: 28px; border-radius: 50%;
    background: var(--red); flex: none;
  }

  /* Back of card */
  .card--back {
    left: 70px; top: 34px;
    background: radial-gradient(circle at 40% 40%, var(--red-light) 0%, var(--red) 55%, var(--red-deep) 100%);
    color: var(--white);
  }
  .card--back .brand {
    position: absolute; left: 180px; top: 146px;
    color: var(--white);
  }
  .card--back .brand__dot { background: var(--white); }
  .venue { position: absolute; font-size: 16px; line-height: 1.2; }
  .venue__title { font-weight: 700; }
  .venue--studio { right: 40px; top: 40px; text-align: right; }
  .venue--outdoor { left: 40px; bottom: 40px; }

  /* Front of card */
  .card--front {
    left: 470px; top: 463px;
    background: var(--paper);
  }
  .card--front .swoosh {
    position: absolute; inset: 0; width: 660px; height: 403px;
  }
  .card--front .brand {
    position: absolute; left: 36px; top: 66px;
  }
  .contact {
    position: absolute; left: 400px; top: 62px;
    color: var(--grey);
  }
  .contact__name { color: var(--red); font-weight: 700; font-size: 19px; }
  .contact__role { font-size: 17px; margin-bottom: 12px; }
  .contact__list { list-style: none; font-size: 18px; line-height: 1.25; }
  .contact__list li { display: flex; align-items: center; gap: 14px; }
  .contact__list svg { width: 14px; height: 14px; flex: none; }
  .abn {
    position: absolute; left: 36px; bottom: 32px;
    color: var(--white); font-size: 17px; letter-spacing: 0.5px;
  }
</style>
</head>
<body>
<main class="canvas">

  <section class="card card--back" aria-label="Back of business card">
    <div class="brand"><span class="brand__dot"></span>TRIMVOLT FITNESS</div>
    <div class="venue venue--studio">
      <p class="venue__title">Personal Training</p>
      <p>Greywater Bay Fitness Studio</p>
      <p>518 Marrowdene Street</p>
      <p>Scarborough WA 6019</p>
    </div>
    <div class="venue venue--outdoor">
      <p class="venue__title">Outdoor Group Training</p>
      <p>Harrowvale Rowing Club</p>
      <p>42 Pellinore Road</p>
      <p>Scarborough WA 6019</p>
    </div>
  </section>

  <section class="card card--front" aria-label="Front of business card">
    <svg class="swoosh" viewBox="0 0 660 403" aria-hidden="true">
      <path d="M0 304 Q330 284 660 240 L660 403 L0 403 Z" fill="var(--red)"/>
      <path d="M0 284 Q330 254 660 224 Q360 272 0 298 Z" fill="var(--black)"/>
    </svg>
    <div class="brand"><span class="brand__dot"></span>TRIMVOLT FITNESS</div>
    <div class="contact">
      <p class="contact__name">Darren Kellworth</p>
      <p class="contact__role">Director</p>
      <ul class="contact__list">
        <li>
          <svg viewBox="0 0 14 14"><path d="M2 5 Q7 1 12 5 L10 7 L9 5 L5 5 L4 7 Z M3 8 H11 V12 H3 Z" fill="var(--red)"/></svg>
          0458 712 064
        </li>
        <li>
          <svg viewBox="0 0 14 14"><rect x="1" y="3" width="12" height="8" fill="none" stroke="var(--red)" stroke-width="1.5"/><path d="M1 3 L7 8 L13 3" fill="none" stroke="var(--red)" stroke-width="1.5"/></svg>
          trimvolt@pelmarix.com
        </li>
        <li>
          <svg viewBox="0 0 14 14"><circle cx="7" cy="7" r="5.5" fill="none" stroke="var(--red)" stroke-width="1.4"/><ellipse cx="7" cy="7" rx="2.4" ry="5.5" fill="none" stroke="var(--red)" stroke-width="1.2"/><path d="M1.5 7 H12.5" stroke="var(--red)" stroke-width="1.2"/></svg>
          trimvoltfitness.net.au
        </li>
      </ul>
    </div>
    <p class="abn">ABN : 47302961</p>
  </section>

</main>
</body>
</html>
```